Book cover - Quiet Rooms, Open Doors

Book cover for Ebook (Pagelight) and wrap around print cover (Printvale) (back, front, and spine)

The book title (may slightly change by end of brief):
(MAIN TITLE) 'Quiet Rooms, Open Doors'
(SUB HEADING) 'A Week-by-Week Practical Workbook to Loosen Nervous Habits, Quieten Doubt and Build Steady Poise'
by Dr Owen Hartley

I would like a bold, stand out cover. Contemporary. I would like to avoid stereotypical images of people looking anxious or worried. I would like the design to be more uplifting and hopeful, rather than focusing on the negative aspect of anxiety, but avoiding cliched photos of people raising their hands in the air, smiling and jumping etc. The cover should appeal to both men and women.

Trim size of book cover (for PrintVale) is 5.25" x 8" back and front with a spine size of 0.477 inches

Reason: I have decided to extend the deadline by 1 more day, not because I am unhappy with the quality of the designs, but because a few designers have contacted me to explain they have had technical difficulties when submitting their files. Thanks everyone for the hard work and great designs.

Target Market(s)

Males and females (16+) who struggle with social anxiety and shyness

Industry/Entity Type

Social

Font styles to use
Serif

Requirements
Must have
• Bold cover that is modern and contemporary. For example, I like these covers:
• http://shrtlnk.example/k4Tq9Zb
• http://shrtlnk.example/m8Wv2Hn
• http://shrtlnk.example/p3Jx6Lr
• http://shrtlnk.example/t7Gd1Qe
• http://shrtlnk.example/v2Nk8Fy
• http://shrtlnk.example/w9Bh4Cs
• http://shrtlnk.example/z5Mf3Ud
Nice to have
• Open to abstract designs.
Should not have
• No stereotypical pictures of people who look anxious or worried. Avoid cliched photos of people raising their hands in the air, smiling and jumping etc.

```html
<!DOCTYPE html>
<html lang="en">
<head>
<meta charset="utf-8">
<title>Quiet Rooms, Open Doors — Book Cover</title>
<link rel="stylesheet" href="https://fonts.googleapis.com/css2?family=Montserrat:wght@400;500&family=Yellowtail&display=swap">
<style>
  :root {
    --stage: #b4b49f;
    --cover-top: #3a78b0;
    --cover-mist: #d6e5e4;
    --cover-aqua: #3ec6cd;
    --cover-deep: #2a95b0;
    --ink-blue: #1f5ea8;
    --ink-aqua: #43cbd3;
    --sub-ink: #1b4c86;
    --author: #ffffff;
  }
  * { margin: 0; padding: 0; box-sizing: border-box; }
  html, body {
    width: 1200px;
    height: 1000px;
    overflow: hidden;
    background: var(--stage);
  }
  .canvas {
    position: relative;
    width: 1200px;
    height: 1000px;
  }
  .cover {
    position: absolute;
    left: 288px;
    top: 25px;
    width: 624px;
    height: 950px;
    overflow: hidden;
    box-shadow: 0 6px 18px rgba(0,0,0,0.25);
    background:
      radial-gradient(ellipse 70% 40% at 50% 42%, rgba(240,246,244,0.85), rgba(240,246,244,0) 100%),
      linear-gradient(180deg,
        var(--cover-top) 0%,
        #6fa2c6 12%,
        var(--cover-mist) 40%,
        #c8e2e2 58%,
        #7fd3d6 72%,
        var(--cover-aqua) 84%,
        var(--cover-deep) 100%);
  }
  .title-frame {
    position: absolute;
    left: 0;
    top: 0;
    width: 624px;
    height: 950px;
  }
  .book-title {
    font-weight: 400;
  }
  .title-kicker {
    position: absolute;
    top: 82px;
    left: 0;
    right: 0;
    text-align: center;
    font-family: "Montserrat", sans-serif;
    font-weight: 500;
    font-size: 46px;
    letter-spacing: 1px;
    color: var(--ink-blue);
    line-height: 1;
  }
  .title-script {
    position: absolute;
    font-family: "Yellowtail", "Brush Script MT", cursive;
    font-weight: 400;
    font-size: 140px;
    color: var(--ink-blue);
    text-shadow: -4px 3px 0 var(--ink-aqua);
    line-height: 1;
    white-space: nowrap;
  }
  .title-rooms { top: 165px; left: 66px; }
  .title-open  { top: 330px; right: 70px; }
  .title-doors { top: 495px; left: 66px; }
  .subtitle {
    position: absolute;
    top: 722px;
    left: 40px;
    right: 40px;
    text-align: center;
    font-family: "Montserrat", sans-serif;
    font-weight: 500;
    font-size: 16.5px;
    line-height: 1.6;
    color: var(--sub-ink);
  }
  .author {
    position: absolute;
    top: 878px;
    left: 0;
    right: 0;
    text-align: center;
    font-family: "Montserrat", sans-serif;
    font-weight: 400;
    font-size: 50px;
    letter-spacing: 2px;
    color: var(--author);
    line-height: 1;
  }
</style>
</head>
<body>
  <main class="canvas">
    <section class="cover" aria-label="Front cover of Quiet Rooms, Open Doors">
      <svg class="title-frame" viewBox="0 0 624 950" aria-hidden="true">
        <path d="M218 105 H38 V670 H586 V105 H406" fill="none" stroke="#1f5ea8" stroke-width="3"/>
      </svg>
      <h1 class="book-title">
        <span class="title-kicker">QUIET</span>
        <span class="title-script title-rooms">Rooms,</span>
        <span class="title-script title-open">Open</span>
        <span class="title-script title-doors">Doors</span>
      </h1>
      <p class="subtitle">A Week-by-Week Practical Workbook to Loosen Nervous<br>Habits, Quieten Doubt and Build Steady Poise</p>
      <p class="author">DR OWEN HARTLEY</p>
    </section>
  </main>
</body>
</html>
```